Pathways to Brightmoor Land Ventures

size of the ad - 8”x 10.75" plus 0.25" bleed
I would like an ad for a magazine that will stand out and make people want to read the ad.
The ad should not be crowded and people reading the ad will be able to read the text.
I would like it to be a creative and modern-day design.
the list of topics should not be the focus of the ad.
the text is attached.
If you decide to use people in the ad then please no ladies.
please note that leave over 1 inch for the bottom of the footer

```html
<!DOCTYPE html>
<html lang="en">
<head>
<meta charset="utf-8">
<title>Pathways to Brightmoor Land Ventures – Course Ad</title>
<link href="https://fonts.googleapis.com/css2?family=Oswald:wght@700&family=Arimo:ital,wght@0,400;0,700;1,400;1,700&display=swap" rel="stylesheet">
<style>
  :root {
    --page-bg: #3b3a3b;
    --sky-light: #8fcbee;
    --sky: #4a9fd8;
    --building-deep: #0d1622;
    --building-mid: #1d3346;
    --building-blue: #24557a;
    --panel: rgba(12, 20, 30, 0.78);
    --white: #ffffff;
    --muted: #c9ccd0;
    --rule: rgba(255, 255, 255, 0.7);
  }
  * { margin: 0; padding: 0; box-sizing: border-box; }
  html, body {
    width: 1200px; height: 1200px; overflow: hidden;
    background: var(--page-bg);
  }
  .ad {
    position: absolute; left: 153px; top: 0;
    width: 894px; height: 1200px;
    overflow: hidden;
    font-family: "Arimo", Arial, sans-serif;
    color: var(--white);
  }
  .ad__photo {
    position: absolute; inset: 0;
    background:
      linear-gradient(90deg, rgba(8,14,22,0.9) 0%, rgba(8,14,22,0.55) 18%, rgba(0,0,0,0) 40%, rgba(0,0,0,0) 70%, rgba(10,25,40,0.6) 100%),
      linear-gradient(180deg, var(--sky-light) 0%, var(--sky) 10%, var(--building-blue) 22%, var(--building-mid) 50%, var(--building-deep) 78%, #2a4860 92%, #3b5f7a 100%);
  }
  .ad__title {
    position: absolute; left: 0; top: 0;
    width: 894px; height: 100px;
    font-size: 0; line-height: 0;
  }
  .ad__title svg { display: block; width: 894px; height: 100px; }
  .ad__title text {
    font-family: "Oswald", "Arial Narrow", sans-serif;
    font-weight: 700; font-size: 112px;
    fill: var(--white);
  }
  .ad__panel {
    position: absolute; left: 164px; top: 124px;
    width: 730px; height: 971px;
    background: var(--panel);
  }
  .course-name {
    position: absolute; left: 206px; top: 170px;
    font-weight: 700; font-size: 44px; line-height: 54px;
    text-transform: uppercase;
  }
  .tagline {
    position: absolute; left: 206px; top: 290px;
    font-style: italic; font-weight: 400; font-size: 31px; line-height: 46px;
    letter-spacing: 3px; text-transform: uppercase;
  }
  .location {
    position: absolute; left: 216px; top: 421px;
    font-weight: 700; font-size: 35px;
  }
  .location-rule {
    position: absolute; left: 206px; top: 472px;
    width: 398px; height: 1px; background: var(--rule);
  }
  .details {
    position: absolute; left: 216px; top: 478px;
    list-style: none;
    font-weight: 700; font-size: 26px; line-height: 37px;
  }
  .early-bird {
    position: absolute; left: 216px; top: 630px;
    font-size: 23px; line-height: 28px;
  }
  .early-bird__label { display: block; font-style: italic; font-weight: 700; color: var(--muted); }
  .topics {
    position: absolute; left: 216px; top: 746px;
    font-size: 21.5px; line-height: 28px;
  }
  .topics__heading { font-weight: 700; font-size: inherit; }
  .topics__list { list-style: none; }
</style>
</head>
<body>
  <article class="ad">
    <div class="ad__photo" role="img" aria-label="Photograph looking up between modern glass office towers against a blue sky, with a street and trees at the bottom"></div>
    <h1 class="ad__title">
      <svg viewBox="0 0 894 100" aria-label="Real Estate Course">
        <text x="0" y="90" textLength="894" lengthAdjust="spacingAndGlyphs">REAL ESTATE COURSE</text>
      </svg>
    </h1>
    <div class="ad__panel"></div>

    <h2 class="course-name">Pathways to Brightmoor<br>Land Ventures</h2>
    <p class="tagline">Investing in knowledge is<br>investing in opportunities.</p>

    <p class="location">Larkfield</p>
    <div class="location-rule"></div>
    <ul class="details">
      <li>10 -Tuesday evenings sessions</li>
      <li>Starting Feb.28</li>
      <li>Limited Partial Scholarships</li>
    </ul>

    <p class="early-bird">
      <span class="early-bird__label">Early Bird Special</span>
      For those that started or would like to go into real estate
    </p>

    <section class="topics">
      <h3 class="topics__heading">Topics: partial listing</h3>
      <ul class="topics__list">
        <li>Real estate investment strategies</li>
        <li>Due diligence</li>
        <li>Financing</li>
        <li>Underwriting</li>
        <li>Property management</li>
        <li>Real estate Legal basics</li>
        <li>Sourcing deals</li>
        <li>Syndication</li>
        <li>Dealing with brokers</li>
        <li>Tax fundamentals</li>
      </ul>
    </section>
  </article>
</body>
</html>
```